CD Cover Art!

I am releasing an EP (3 song CD) and a full length CD (9 songs) and would like to have 2 distinct yet somehow tied together CD covers... they could be tied together through a simple color scheme or via tricky titles or through a shared logo designed around my name (Dane Harlow) or some other method of your imagination. I am not expecting two distinctly different covers, please design one and borrow from it to design the other which should simply the design greatly and insure I have no problem branding myself.

I will have some photos you can use soon or look at www.ravenbarker.example for some ideas although please be aware these CD's are not for Dane Harlow and The Drifters... this is design is for just "Dane Harlow"

My new Website should be up soon, please check it for design references www.DaneHarlow.example

Reason: Due to lack of designs submissions I've increased the budget and am guaranteeing payment, this is my first time using a service like this so I'm just learning the ropes!

Target Market(s)

Rock and Blues music lovers.

Font styles to use
Other font styles liked:
• Earth Kid

Requirements
Must have
• Title and or logo on both CD's

Name of the EP CD will be "Velvet Horizon" and the full length CD will be called "Dane Harlow Collection"
"Earth Kid" is the name of the font used on my website, I'd like to use it for consistency on both CD Covers.
Nice to have
• I love crosses and birds of prey, motorcycles and I really like Morrow's album art although I am not latino and wouldn't want a latino-style. I just love the colors and art-work. My design does not have to have any one or all of these items but I like them!

If desired I can provide a picture of my motorcycle if you are going to include one in the design it might as well be mine.

```html
<!DOCTYPE html>
<html lang="en">
<head>
<meta charset="utf-8">
<title>Dane Harlow – Velvet Horizon</title>
<link rel="stylesheet" href="https://fonts.googleapis.com/css2?family=Black+Ops+One&display=swap">
<style>
  :root {
    --page: #ffffff;
    --ink: #ffffff;
    --glow: rgba(255, 250, 235, 0.85);
    --space-dark: #120d08;
    --teal: #2a8f9a;
    --sky-blue: #3f8fe0;
    --haze: #f3e6da;
    --amber: #e08a1e;
    --ember: #b8381c;
    --moss: #2f5a2a;
    --umber: #4a2a10;
  }

  * { margin: 0; padding: 0; box-sizing: border-box; }

  html, body {
    width: 1200px;
    height: 1000px;
    overflow: hidden;
    background: var(--page);
  }

  .canvas {
    position: relative;
    width: 1200px;
    height: 1000px;
    background: var(--page);
  }

  .cover {
    position: absolute;
    left: 100px;
    top: 0;
    width: 1000px;
    height: 1000px;
    overflow: hidden;
    background: var(--space-dark);
  }

  .cover-art {
    position: absolute;
    inset: 0;
    background:
      radial-gradient(ellipse 22% 16% at 68% 27%, rgba(255, 245, 240, 0.85), transparent 70%),
      radial-gradient(ellipse 30% 22% at 52% 12%, var(--teal), transparent 75%),
      radial-gradient(ellipse 28% 30% at 78% 30%, var(--sky-blue), transparent 72%),
      radial-gradient(ellipse 24% 20% at 28% 78%, rgba(70, 140, 230, 0.9), transparent 72%),
      radial-gradient(ellipse 34% 26% at 70% 72%, var(--amber), transparent 72%),
      radial-gradient(ellipse 24% 18% at 55% 95%, var(--ember), transparent 75%),
      radial-gradient(ellipse 30% 30% at 18% 22%, var(--moss), transparent 75%),
      radial-gradient(ellipse 26% 28% at 10% 90%, #b9801e, transparent 75%),
      radial-gradient(ellipse 30% 30% at 95% 60%, var(--umber), transparent 75%),
      radial-gradient(ellipse 60% 40% at 50% 50%, rgba(180, 120, 70, 0.55), transparent 80%),
      var(--space-dark);
  }

  .eagle-art {
    position: absolute;
    left: 390px;
    top: 680px;
    width: 460px;
    height: 200px;
    border-radius: 50%;
    background: radial-gradient(ellipse at 60% 55%, rgba(90, 50, 20, 0.75), rgba(60, 35, 15, 0.35) 55%, transparent 75%);
  }

  .title-block {
    position: absolute;
    left: 70px;
    top: 0;
    color: var(--ink);
    font-family: "Black Ops One", "Arial Black", sans-serif;
    text-transform: uppercase;
    text-shadow: 0 0 14px var(--glow), 0 0 34px rgba(255, 240, 210, 0.45);
    white-space: nowrap;
  }

  .artist-name {
    position: absolute;
    top: 256px;
    left: 0;
    font-size: 82px;
    line-height: 1;
    letter-spacing: 2px;
  }

  .album-title {
    position: absolute;
    left: 0;
    font-size: 164px;
    line-height: 1;
    letter-spacing: 4px;
  }

  .album-title--first { top: 338px; }
  .album-title--second { top: 497px; }
</style>
</head>
<body>
  <main class="canvas">
    <section class="cover">
      <div class="cover-art" role="img" aria-label="Colourful cosmic nebula in teal, blue, amber and red over a dusty mountain horizon"></div>
      <div class="eagle-art" role="img" aria-label="Bald eagle soaring with wings spread"></div>
      <div class="title-block">
        <p class="artist-name">Dane Harlow</p>
        <h1 class="album-title album-title--first">Velvet</h1>
        <h1 class="album-title album-title--second">Horizon</h1>
      </div>
    </section>
  </main>
</body>
</html>
```